New webpage design for development bureau

We are a development bureau in Denmark, and need a design for our webpage. We are called Harbor Development (Part of Harbor Fjeld Skolium Group), and are going to aim for multiple markets: Web, Apps, Desktop applications, ect.

We already have a logo, see the uploaded file. We do not have any special demands, other than in have to be simple. A portfolio view should also be available, for future customers.

```html
<!DOCTYPE html>
<html lang="en">
<head>
<meta charset="utf-8">
<title>Harbor Development</title>
<link href="https://fonts.googleapis.com/css2?family=Oxygen:wght@300;400;700&display=swap" rel="stylesheet">
<style>
:root{
  --blue:#1aa7e2;
  --orange:#f7931e;
  --ink:#2b2b2b;
  --text:#3a3a3a;
  --hero:#7b7c80;
  --footer:#4a4a4a;
  --tab:#d4d4d4;
  --tile-bar:#2e2e2e;
  --white:#fff;
}
*{box-sizing:border-box;margin:0;padding:0}
html,body{width:827px;height:1200px;overflow:hidden;background:var(--white)}
body{position:relative;font-family:"Oxygen",Arial,sans-serif;color:var(--text)}

/* header */
.site-header{position:absolute;left:0;top:0;width:827px;height:38px;background:linear-gradient(#fff,#f1f1f1);box-shadow:0 1px 3px rgba(0,0,0,.25);z-index:2}
.brand{position:absolute;left:82px;top:10px;font-weight:700;font-size:17px;letter-spacing:.5px;color:var(--ink)}
.main-nav a{position:absolute;top:0;height:38px;line-height:38px;font-size:9.5px;color:#444;text-decoration:none}
.main-nav a.active{background:var(--blue);color:var(--white);text-align:center}
.social{position:absolute;display:flex;gap:1px}
.social span{width:14px;height:14px;border-radius:50%;background:#b7b7b7}
.social span:first-child{background:#333}

/* hero */
.hero{position:absolute;left:0;top:38px;width:827px;height:376px;background:var(--hero);overflow:hidden}
.hero-visual{position:absolute;left:300px;top:0;width:527px;height:376px;
  background:
    radial-gradient(ellipse 150px 110px at 300px 200px,rgba(160,205,235,.55),rgba(160,205,235,0) 70%),
    radial-gradient(ellipse 120px 60px at 420px 300px,rgba(140,195,230,.45),rgba(140,195,230,0) 70%),
    linear-gradient(90deg,var(--hero) 0%,#8d9095 18%,#b3bac1 40%,#d6dde3 65%,#e9edf0 85%,#f2f4f6 100%)}
.welcome-rule{position:absolute;left:82px;top:116px;width:272px;border-top:1px dotted #cfcfcf}
.welcome-tag{position:absolute;left:187px;top:109px;width:63px;height:15px;background:#3b3b3b;color:#eee;font-size:7.5px;line-height:15px;text-align:center}
.hero-title{position:absolute;left:82px;top:132px;width:272px;text-align:center;color:var(--white);font-weight:400;font-size:26px;line-height:32px;white-space:nowrap}
.cta{position:absolute;left:157px;top:206px;width:122px;height:31px;background:var(--blue);color:var(--white);font-weight:700;font-size:12.5px;line-height:31px;text-align:center}
.learn{color:var(--orange);font-size:10.5px}
.hero .learn{position:absolute;left:157px;top:246px;width:122px;text-align:center}
.dots{position:absolute;left:82px;top:328px;display:flex;gap:2px}
.dots span{width:7px;height:7px;border-radius:50%;background:var(--white)}
.dots span.on{background:var(--orange)}

/* services */
.section-title{position:absolute;left:0;width:827px;text-align:center;font-size:19px;font-weight:400}
.services-title{top:472px;color:var(--blue)}
.title-rule{position:absolute;left:238px;top:509px;width:352px;border-top:1px dotted #555}
.title-mark{position:absolute;left:402px;top:507px;width:23px;height:5px;background:#111}
.service{position:absolute;top:556px;width:180px;text-align:center}
.service svg{display:block;margin:0 auto}
.service h3{font-weight:400;font-size:12.5px;color:#444;margin-top:10px}
.service p{font-size:8.6px;line-height:12.5px;color:#333;margin-top:5px}
.service .learn{display:block;margin-top:6px;font-size:10px}

/* portfolio */
.portfolio-title{top:803px;color:#111}
.tabs{position:absolute;left:262px;top:842px;height:24px;display:flex;gap:2px}
.tab{height:24px;line-height:24px;text-align:center;font-size:12px;color:#fff;background:var(--tab)}
.tab.active{background:var(--blue)}
.tile{position:absolute;overflow:hidden}
.tile .shot{position:absolute;inset:0}
.tile .bar{position:absolute;left:0;right:0;bottom:0;height:20px;background:var(--tile-bar);color:#eee;font-size:7.5px;line-height:20px;padding-left:9px}
.go{position:absolute;right:5px;bottom:5px;width:11px;height:9px;background:var(--orange)}
.go svg{display:block}
.feature .bar{height:40px;line-height:11px;padding:10px 13px 0}
.feature .bar b{font-weight:400;font-size:8.5px;display:block}

/* footer */
.site-footer{position:absolute;left:0;top:1172px;width:827px;height:28px;background:var(--footer);color:#ddd;font-size:7.5px}
.site-footer .links{position:absolute;left:83px;top:10px;display:flex;gap:11px}
.site-footer .legal{position:absolute;left:552px;top:10px}
</style>
</head>
<body>

<header class="site-header">
  <div class="brand">HARBOR</div>
  <nav class="main-nav">
    <a style="left:314px">HOME</a>
    <a class="active" style="left:351px;width:65px">ABOUT US</a>
    <a style="left:426px">SERVICES</a>
    <a style="left:489px">PORTFOLIO</a>
    <a style="left:559px">OUR TEAM</a>
    <a style="left:626px">CONTACT US</a>
  </nav>
  <div class="social" style="left:701px;top:13px"><span></span><span></span><span></span></div>
</header>

<section class="hero">
  <div class="hero-visual" role="img" aria-label="Photo of a man in a striped shirt holding a floating laptop, globe, phone and tablet connected by network lines"></div>
  <div class="welcome-rule"></div>
  <div class="welcome-tag">WELCOME TO</div>
  <h1 class="hero-title">Harbor Software and<br>Development Company</h1>
  <div class="cta">Call to Action</div>
  <div class="learn">Learn More »</div>
  <div class="dots"><span></span><span class="on"></span><span></span></div>
</section>

<h2 class="section-title services-title">Our Services</h2>
<div class="title-rule"></div>
<div class="title-mark"></div>

<div class="service" style="left:112px">
  <svg width="140" height="104" viewBox="0 0 140 104">
    <rect x="22" y="20" width="97" height="70" rx="2" fill="none" stroke="#444" stroke-width="4"/>
    <path d="M6 89h130v3a3 3 0 0 1-3 3H9a3 3 0 0 1-3-3z" fill="#444"/>
    <rect x="62" y="89" width="18" height="2" fill="#999"/>
    <circle cx="119" cy="22" r="9" fill="#fff" stroke="#444" stroke-width="1.5"/>
    <circle cx="119" cy="22" r="5" fill="#444"/>
  </svg>
  <h3>Web Application</h3>
  <p>Lorem ipsum dolor sit amet, consectetur adipisicing elit, sed do eiusmod tempor incididunt ut et dolore</p>
  <span class="learn">Learn More »</span>
</div>

<div class="service" style="left:324px">
  <svg width="140" height="104" viewBox="0 0 140 104">
    <rect x="47" y="11" width="46" height="84" rx="5" fill="#444"/>
    <rect x="52" y="20" width="36" height="64" fill="#fff"/>
    <rect x="62" y="14" width="16" height="2" rx="1" fill="#aaa"/>
    <circle cx="92" cy="12" r="9" fill="#fff" stroke="#444" stroke-width="1.5"/>
    <circle cx="92" cy="12" r="5" fill="#444"/>
  </svg>
  <h3>App Application</h3>
  <p>Lorem ipsum dolor sit amet, consectetur adipisicing elit, sed do eiusmod tempor incididunt ut et dolore</p>
  <span class="learn">Learn More »</span>
</div>

<div class="service" style="left:535px">
  <svg width="140" height="104" viewBox="0 0 140 104">
    <rect x="23" y="16" width="94" height="62" rx="5" fill="#444"/>
    <rect x="31" y="23" width="78" height="46" fill="#fff"/>
    <rect x="63" y="78" width="14" height="12" fill="#444"/>
    <path d="M46 96q24-10 48 0z" fill="#444"/>
    <circle cx="110" cy="18" r="9" fill="#fff" stroke="#444" stroke-width="1.5"/>
    <circle cx="110" cy="18" r="5" fill="#444"/>
  </svg>
  <h3>Desktop Application</h3>
  <p>Lorem ipsum dolor sit amet, consectetur adipisicing elit, sed do eiusmod tempor incididunt ut et dolore</p>
  <span class="learn">Learn More »</span>
</div>

<h2 class="section-title portfolio-title">Our Portfolio</h2>
<div class="tabs">
  <div class="tab active" style="width:68px">Web</div>
  <div class="tab" style="width:69px">Apps</div>
  <div class="tab" style="width:156px">Desktop Application</div>
</div>

<div class="tile feature" style="left:104px;top:891px;width:241px;height:219px">
  <div class="shot" role="img" aria-label="Resume promotion website preview with a young man leaning on a white wall" style="background:linear-gradient(90deg,#e6e6e4,#d9d9d6 60%,#cfcfcb)"></div>
  <div class="bar"><b>Resume Promotion</b>Lorem ipsum dolor sit amet, consectetur... Learn More</div>
  <div class="go"><svg width="11" height="9" viewBox="0 0 11 9"><path d="M2 4.5h6M6 2l2.5 2.5L6 7" stroke="#fff" stroke-width="1.4" fill="none"/></svg></div>
</div>

<div class="tile" style="left:356px;top:891px;width:116px;height:103px">
  <div class="shot" role="img" aria-label="Light blue agency website preview" style="background:linear-gradient(#5fd0ef,#3cb5e0)"></div>
  <div class="bar">Lorem Ipsum Text</div>
  <div class="go" style="background:var(--blue)"><svg width="11" height="9" viewBox="0 0 11 9"><path d="M2 4.5h6M6 2l2.5 2.5L6 7" stroke="#fff" stroke-width="1.4" fill="none"/></svg></div>
</div>
<div class="tile" style="left:482px;top:891px;width:116px;height:103px">
  <div class="shot" role="img" aria-label="Sports website preview with a cyclist" style="background:linear-gradient(120deg,#3a3a44,#8a6f6a 55%,#c5a592)"></div>
  <div class="bar">Lorem Ipsum Text</div>
  <div class="go"><svg width="11" height="9" viewBox="0 0 11 9"><path d="M2 4.5h6M6 2l2.5 2.5L6 7" stroke="#fff" stroke-width="1.4" fill="none"/></svg></div>
</div>
<div class="tile" style="left:607px;top:891px;width:116px;height:103px">
  <div class="shot" role="img" aria-label="Dark monochrome welcome website preview" style="background:linear-gradient(160deg,#555,#222)"></div>
  <div class="bar">Lorem Ipsum Text</div>
  <div class="go"><svg width="11" height="9" viewBox="0 0 11 9"><path d="M2 4.5h6M6 2l2.5 2.5L6 7" stroke="#fff" stroke-width="1.4" fill="none"/></svg></div>
</div>
<div class="tile" style="left:356px;top:1007px;width:116px;height:103px">
  <div class="shot" role="img" aria-label="Nightlife website preview with a crowd" style="background:linear-gradient(#f2f2f2 0 12%,#4a3a42 12%,#2a2228)"></div>
  <div class="bar">Lorem Ipsum Text</div>
  <div class="go"><svg width="11" height="9" viewBox="0 0 11 9"><path d="M2 4.5h6M6 2l2.5 2.5L6 7" stroke="#fff" stroke-width="1.4" fill="none"/></svg></div>
</div>
<div class="tile" style="left:482px;top:1007px;width:116px;height:103px">
  <div class="shot" role="img" aria-label="Colourful children's blog website preview" style="background:linear-gradient(#f6e27a 0 10%,#e8f4f8 10% 70%,#a8d66a 70%)"></div>
  <div class="bar">Lorem Ipsum Text</div>
  <div class="go"><svg width="11" height="9" viewBox="0 0 11 9"><path d="M2 4.5h6M6 2l2.5 2.5L6 7" stroke="#fff" stroke-width="1.4" fill="none"/></svg></div>
</div>
<div class="tile" style="left:607px;top:1007px;width:116px;height:103px">
  <div class="shot" role="img" aria-label="Castle and garden website preview" style="background:linear-gradient(#b8d4e8,#8fb0c0 45%,#5f8a3a 60%,#3f6e26)"></div>
  <div class="bar">Lorem Ipsum Text</div>
  <div class="go"><svg width="11" height="9" viewBox="0 0 11 9"><path d="M2 4.5h6M6 2l2.5 2.5L6 7" stroke="#fff" stroke-width="1.4" fill="none"/></svg></div>
</div>

<footer class="site-footer">
  <div class="links"><span>HOME</span><span>ABOUT US</span><span>SERVICES</span><span>PORTFOLIO</span><span>OUR TEAM</span><span>CONTACT US</span></div>
  <div class="legal">© Copyright 2014 &nbsp;-&nbsp; Terms and Conditions</div>
  <div class="social" style="left:701px;top:7px"><span style="background:#111"></span><span></span><span></span></div>
</footer>

</body>
</html>
```